New brand BrioNoodla needs a Web Design

BrioNoodla is the new brand for Russian market. Our pasta is an innovative product (contains only 6 calories per portion). BrioNoodla gives you a way of enjoying your favorite pasta recipe without the calorie. You can eat and lose weight. All natural ingredients.

Our mission:
You can enjoy your favorite pasta and the same time to be fit.

Task
Now we have our site: http://brionoodla.example.ru/site/
But we want to make a new alternative design with an emphasis on Italian cuisine.
You use the same photos and texts or use others photos what you think.

We want to try aggressive colors like sport nutrition.
We will sell 5 kind of product: Spaghetti, Noodles, Fettuccine, Lasagna, Rice. And we have 5 different packs for each one. You can use the pack colors.

Target Market(s)

Individuals who want to lose weight , take care of themselves, sportsmen.

Industry/Entity Type

Product

Number of Pages Required

5+ page

Requirements
Must have
• Bright aggressive colors like the our packs.
Nice to have
• We want to try aggressive colors like sport nutrition.
Should not have
• There should be no association with Chinese noodles.

```html
<!DOCTYPE html>
<html lang="ru">
<head>
<meta charset="utf-8">
<title>BrioNoodla — всего 6 ккал в порции</title>
<link href="https://fonts.googleapis.com/css2?family=Lato:wght@300;400;700&display=swap" rel="stylesheet">
<style>
  :root {
    --wood-dark: #4a2e1c;
    --wood-mid: #7a5135;
    --wood-light: #9a6a45;
    --header-green: rgba(120, 160, 40, 0.82);
    --accent-orange: #d64a17;
    --accent-orange-text: #f2b233;
    --accent-yellow: #efbf2f;
    --accent-yellow-text: #d8541a;
    --accent-red: #c20b0b;
    --olive: #6e8a1c;
    --olive-text: #7c9a2a;
    --icon-yellow: #f0c020;
    --white: #ffffff;
    --page: #ffffff;
    --rule: #edbd22;
  }
  * { box-sizing: border-box; margin: 0; padding: 0; }
  html, body { width: 960px; height: 1200px; overflow: hidden; background: var(--page); }
  body { position: relative; font-family: 'Lato', sans-serif; }

  .hero {
    position: absolute; left: 0; top: 0; width: 960px; height: 692px;
    background:
      linear-gradient(180deg, rgba(90,120,40,0.55) 0%, rgba(90,120,40,0.0) 38%),
      linear-gradient(90deg, var(--wood-mid) 0%, var(--wood-light) 30%, var(--wood-mid) 55%, var(--wood-light) 80%, var(--wood-dark) 100%);
  }
  .site-header {
    position: absolute; left: 0; top: 0; width: 960px; height: 118px;
    background: var(--header-green);
    display: flex; align-items: center; justify-content: space-between;
    padding: 0 30px 0 26px;
  }
  .brand {
    color: var(--white); font-weight: 300; font-size: 36px; letter-spacing: 0.5px;
  }
  .main-nav { display: flex; gap: 25px; }
  .main-nav a {
    color: var(--white); text-decoration: none; font-weight: 700; font-size: 15px;
    text-transform: uppercase; letter-spacing: 0.2px;
  }
  .product-pack {
    position: absolute; left: 112px; top: 272px; width: 252px; height: 388px;
    border-radius: 8px;
    background: linear-gradient(90deg, #3ea2de 0%, #1e1e1e 14%, #2c2c2c 50%, #1e1e1e 86%, #3ea2de 100%);
    box-shadow: 0 10px 24px rgba(0,0,0,0.4);
  }
  .hero-headline {
    position: absolute; left: 414px; top: 339px; width: 512px; height: 75px;
    background: var(--accent-orange); color: var(--accent-orange-text);
    font-weight: 300; font-size: 44px; line-height: 75px; padding-left: 22px;
    white-space: nowrap;
  }
  .hero-cta {
    position: absolute; left: 414px; top: 414px; width: 320px; height: 49px;
    background: var(--accent-yellow); color: var(--accent-yellow-text);
    font-weight: 300; font-size: 20px; line-height: 49px; padding-left: 24px;
  }
  .kcal-badge {
    position: absolute; left: 414px; top: 520px; width: 198px; height: 100px;
    background: var(--accent-red); color: var(--white);
    display: flex; align-items: center; padding-left: 22px; gap: 14px;
  }
  .kcal-badge__number { font-weight: 300; font-size: 68px; line-height: 1; }
  .kcal-badge__unit { font-size: 33px; font-weight: 400; line-height: 1; }
  .kcal-badge__note { font-size: 16px; font-weight: 400; margin-top: 4px; }

  .benefits { position: absolute; left: 0; top: 692px; width: 960px; height: 502px; }
  .benefits__title {
    position: absolute; left: 0; top: 62px; width: 960px; text-align: center;
    color: var(--olive); font-weight: 300; font-size: 46px;
  }
  .benefit { position: absolute; width: 200px; text-align: center; }
  .benefit svg { display: block; margin: 0 auto; }
  .benefit__label {
    margin-top: 10px; color: var(--olive-text); font-weight: 300; font-size: 18px;
  }
  .footer-rule { position: absolute; left: 0; top: 1194px; width: 960px; height: 6px; background: var(--rule); }
</style>
</head>
<body>
  <section class="hero">
    <div class="hero__photo" role="img" aria-label="Деревянный стол с зеленью, перцем, бадьяном и пряностями" style="position:absolute;inset:0;"></div>

    <header class="site-header">
      <div class="brand">BrioNoodla</div>
      <nav class="main-nav">
        <a href="#">О BrioNoodla</a>
        <a href="#">Купить</a>
        <a href="#">Доставка и оплата</a>
        <a href="#">Рецепты</a>
        <a href="#">Контакты</a>
      </nav>
    </header>

    <div class="product-pack" role="img" aria-label="Упаковка конжак-спагетти BrioNoodla, 6 ккал в порции"></div>

    <h1 class="hero-headline">Всего 6 ккал в порции</h1>
    <div class="hero-cta">Попробуй прямо сейчас</div>
    <div class="kcal-badge">
      <span class="kcal-badge__number">6</span>
      <span>
        <span class="kcal-badge__unit">ККАЛ</span><br>
        <span class="kcal-badge__note">В ПОРЦИИ</span>
      </span>
    </div>
  </section>

  <section class="benefits">
    <h2 class="benefits__title">Всего 6 ккал в порции</h2>

    <div class="benefit" style="left:144px;top:158px;">
      <svg width="72" height="72" viewBox="0 0 72 72"><rect x="26" y="28" width="14" height="18" rx="2" fill="var(--icon-yellow)" transform="rotate(35 33 37)"/><circle cx="36" cy="36" r="32" fill="none" stroke="var(--olive)" stroke-width="6"/><line x1="14" y1="14" x2="58" y2="58" stroke="var(--olive)" stroke-width="6"/></svg>
      <div class="benefit__label">Без сахара</div>
    </div>
    <div class="benefit" style="left:379px;top:158px;">
      <svg width="72" height="72" viewBox="0 0 72 72"><ellipse cx="36" cy="36" rx="10" ry="7" fill="var(--icon-yellow)" transform="rotate(-35 36 36)"/><polygon points="22,40 28,30 30,42" fill="var(--icon-yellow)"/><polygon points="50,32 44,42 42,30" fill="var(--icon-yellow)"/><circle cx="36" cy="36" r="32" fill="none" stroke="var(--olive)" stroke-width="6"/><line x1="14" y1="14" x2="58" y2="58" stroke="var(--olive)" stroke-width="6"/></svg>
      <div class="benefit__label">Без сахара</div>
    </div>
    <div class="benefit" style="left:614px;top:158px;">
      <svg width="72" height="72" viewBox="0 0 72 72"><line x1="30" y1="48" x2="42" y2="24" stroke="var(--icon-yellow)" stroke-width="3"/><ellipse cx="40" cy="30" rx="3" ry="5" fill="var(--icon-yellow)"/><ellipse cx="35" cy="37" rx="3" ry="5" fill="var(--icon-yellow)"/><circle cx="36" cy="36" r="32" fill="none" stroke="var(--olive)" stroke-width="6"/><line x1="14" y1="14" x2="58" y2="58" stroke="var(--olive)" stroke-width="6"/></svg>
      <div class="benefit__label">Без глютена</div>
    </div>

    <div class="benefit" style="left:144px;top:318px;">
      <svg width="72" height="72" viewBox="0 0 72 72"><rect x="26" y="28" width="14" height="18" rx="2" fill="var(--icon-yellow)" transform="rotate(35 33 37)"/><circle cx="36" cy="36" r="32" fill="none" stroke="var(--olive)" stroke-width="6"/><line x1="14" y1="14" x2="58" y2="58" stroke="var(--olive)" stroke-width="6"/></svg>
      <div class="benefit__label">Без жира</div>
    </div>
    <div class="benefit" style="left:379px;top:318px;">
      <svg width="72" height="72" viewBox="0 0 72 72"><rect x="33" y="18" width="6" height="24" rx="3" fill="var(--icon-yellow)"/><circle cx="36" cy="50" r="4" fill="var(--icon-yellow)"/><circle cx="36" cy="36" r="32" fill="none" stroke="var(--olive)" stroke-width="6"/><line x1="14" y1="14" x2="58" y2="58" stroke="var(--olive)" stroke-width="6"/></svg>
      <div class="benefit__label">Без консервантов</div>
    </div>
    <div class="benefit" style="left:614px;top:318px;">
      <svg width="72" height="72" viewBox="0 0 72 72"><path d="M36 54 C18 42 16 30 24 24 C30 20 34 24 36 28 C38 24 42 20 48 24 C56 30 54 42 36 54 Z" fill="var(--icon-yellow)"/><circle cx="36" cy="36" r="32" fill="none" stroke="var(--olive)" stroke-width="6"/><line x1="14" y1="14" x2="58" y2="58" stroke="var(--olive)" stroke-width="6"/></svg>
      <div class="benefit__label">Без холестерина</div>
    </div>
  </section>

  <div class="footer-rule"></div>
</body>
</html>
```